Fiber Optic Internet flyer promotion Winter 2016-2017

I am looking for a marketing flyer that will not be folded, single sided that will advertise a Fiber Optic internet promotion that we are currently running.

The design should be clean, flow well, quickly grab attention, and if a very few short seconds list what the promotion is, and direct them to contact us.

It needs to list a few features of the promotion, but does not need to be in this order and should flow well with the flyer
1.) Fiber Optic Internet
2.) 100 Mbits for $140 /month or 150 Mbits for $190 /month
3.) Free construction cost up to $10,000, limited funds available.
4.) Limited time offer. Must commit before funds run out.

(555) 274-3916, www.kelvoranet.example

Target Market(s)

Small to large business

Industry/Entity Type

Internet Service Provider

Requirements
Must have
• Eye catching appeal. Quickly convey the message of the promotion and our company name and phone number.
Should not have
• Our company is primarily a wireless ISP. This promotion is all about Fiber Optic. I do not want to draw attention to the "wireless" portion of our business with this flyer.

```html
<!DOCTYPE html>
<html lang="en">
<head>
<meta charset="utf-8">
<title>Kelvora Net – Fiber Optic Internet</title>
<link rel="stylesheet" href="https://fonts.googleapis.com/css2?family=Arimo:wght@400;700&family=Montserrat:wght@600&display=swap">
<style>
  :root{
    --violet-light:#cfc9ea;
    --violet-mid:#7464b4;
    --violet-deep:#3c2c7c;
    --violet-ink:#2e2268;
    --white:#ffffff;
    --signal-red:#d42234;
    --brand-navy:#1d2a86;
  }
  html,body{margin:0;padding:0;overflow:hidden;}
  body{width:849px;height:1200px;}
  .flyer{
    position:relative;width:849px;height:1200px;overflow:hidden;
    background:
      radial-gradient(ellipse 520px 420px at 160px 380px, rgba(240,238,250,.95), rgba(240,238,250,0) 70%),
      linear-gradient(160deg,var(--violet-light) 0%,var(--violet-mid) 38%,var(--violet-deep) 78%,var(--violet-ink) 100%);
    font-family:"Arimo",Arial,sans-serif;color:var(--white);
  }
  .fiber-photo{
    position:absolute;left:230px;top:160px;width:619px;height:400px;
    background:radial-gradient(ellipse 320px 170px at 300px 210px, rgba(205,120,200,.55), rgba(160,110,200,.25) 55%, rgba(120,90,180,0) 80%);
  }
  .layout{position:absolute;inset:0;}
  .brand-box{
    position:absolute;left:64px;top:46px;width:244px;height:124px;
    display:flex;align-items:center;justify-content:center;gap:8px;
  }
  .brand-mark{width:16px;height:16px;border-radius:50%;background:var(--signal-red);}
  .brand-name{font-weight:700;font-size:20px;letter-spacing:1px;color:var(--brand-navy);}
  .contact{
    position:absolute;top:80px;left:390px;font-size:18px;display:flex;align-items:center;gap:6px;
  }
  .contact .sep{margin:0 14px;}
  .construction{
    position:absolute;left:40px;width:768px;top:962px;height:50px;
    display:flex;align-items:center;justify-content:center;font-size:22.5px;
  }
  .offer-band{
    position:absolute;left:82px;top:1054px;width:686px;height:64px;background:var(--signal-red);
    display:flex;align-items:center;justify-content:center;font-size:22.5px;
  }
  b{font-weight:700;}
</style>
</head>
<body>
<div class="flyer">
  <div class="fiber-photo" role="img" aria-label="Close-up photo of a bundle of glowing violet fiber optic strands sweeping across the page"></div>

  <svg class="layout" width="849" height="1200" viewBox="0 0 849 1200" aria-hidden="false">
    <defs>
      <pattern id="hatch" width="6" height="6" patternUnits="userSpaceOnUse" patternTransform="rotate(-45)">
        <rect width="6" height="6" fill="none"/>
        <line x1="0" y1="0" x2="0" y2="6" stroke="#fff" stroke-width="2"/>
      </pattern>
    </defs>
    <g fill="none" stroke="#fff" stroke-width="1.6">
      <!-- frame -->
      <path d="M64 106 H40 V1158 H808 V106 H308"/>
      <rect x="64" y="46" width="244" height="124"/>
      <line x1="40" y1="962" x2="808" y2="962"/>
      <line x1="40" y1="1012" x2="808" y2="1012"/>
      <rect x="72" y="1044" width="704" height="82" stroke-dasharray="5 5" stroke-width="1.4"/>
    </g>

    <!-- headline -->
    <g class="headline" fill="#fff">
      <text transform="translate(164 928) rotate(-90)" font-family="Montserrat, sans-serif" font-weight="600" font-size="100" textLength="676" lengthAdjust="spacingAndGlyphs">FIBER OPTIC</text>
      <text transform="translate(214 582) rotate(-90)" font-family="Arimo, sans-serif" font-size="28" textLength="326" letter-spacing="20">INTERNET</text>
    </g>

    <!-- price badges -->
    <g class="price-badges" fill="none" stroke="#fff" stroke-width="3">
      <path d="M535.9 576.4 A108 108 0 1 0 531.5 676"/>
      <path d="M556.5 624 A108 108 0 1 1 556.5 732"/>
      <line x1="570" y1="550" x2="516" y2="754" stroke-width="1.6"/>
      <circle cx="543" cy="652" r="22" fill="var(--violet-mid)" stroke-width="1.8"/>
    </g>
    <rect x="430" y="732" width="19" height="230" fill="url(#hatch)" stroke="#fff" stroke-width="1.6"/>
    <rect x="641" y="788" width="19" height="174" fill="url(#hatch)" stroke="#fff" stroke-width="1.6"/>

    <g fill="#fff" font-family="Arimo, sans-serif" text-anchor="middle">
      <text x="543" y="658" font-size="18">or</text>
      <text x="439" y="580" font-size="24">100 Mbits</text>
      <text x="439" y="603" font-size="18">for</text>
      <text x="439" y="670" font-size="68" font-weight="700"><tspan font-size="36" dy="-2">$</tspan><tspan dy="2">140</tspan></text>
      <text x="439" y="697" font-size="19">/month</text>
      <text x="650" y="636" font-size="24">150 Mbits</text>
      <text x="650" y="659" font-size="18">for</text>
      <text x="650" y="726" font-size="68" font-weight="700"><tspan font-size="36" dy="-2">$</tspan><tspan dy="2">190</tspan></text>
      <text x="650" y="753" font-size="19">/month</text>
    </g>

    <!-- contact icons -->
    <g fill="none" stroke="#fff" stroke-width="1.4">
      <circle cx="541" cy="91" r="8.5"/>
      <path d="M537 87 q0 6 6 8 l1.5-1.8 -2-1.5 -1 1 q-2-1 -2.5-3 l1-1 -1.5-2z" fill="#fff" stroke="none"/>
      <circle cx="797" cy="91" r="9"/>
      <ellipse cx="797" cy="91" rx="4" ry="9"/>
      <line x1="788" y1="91" x2="806" y2="91"/>
      <line x1="790" y1="86" x2="804" y2="86"/>
      <line x1="790" y1="96" x2="804" y2="96"/>
    </g>
  </svg>

  <div class="brand-box">
    <span class="brand-mark"></span>
    <span class="brand-name">KELVORA NET</span>
  </div>

  <div class="contact">
    <span class="phone">(555) 274-3916</span>
    <span style="width:22px"></span>
    <span class="sep">|</span>
    <span class="web">www.kelvoranet.example</span>
  </div>

  <div class="construction"><span><b>Free construction</b> cost up to <b>$10,000</b>, limited funds available</span></div>

  <div class="offer-band"><span><b>Limited time offer.</b> Must commit before funds run out.</span></div>
</div>
</body>
</html>
```